Brava Nest (Smart Home, Installation, Repair Industry) (Contest)

Looking for a website design for my company
Services we offer:
Phone Repair
TV Mounting
Security Camera Installation
Networking / Wi-Fi
Smart Home Services
IT Support

Looking for a website similar to trovely.example

Few tabs
About Us
Contact Us
Areas Served
Pricing and Services

```html
<!DOCTYPE html>
<html lang="en">
<head>
<meta charset="utf-8">
<title>Brava Nest — Home maintenance made simple</title>
<link href="https://fonts.googleapis.com/css2?family=Catamaran:wght@300;400;500;600;700&family=Barlow:wght@400;500;600&display=swap" rel="stylesheet">
<style>
:root{
  --orange:#f7941d;
  --orange-deep:#f08a12;
  --ink:#2e2e2e;
  --text:#444;
  --muted:#777;
  --card:#e4e4e4;
  --line:#bdbdbd;
  --white:#fff;
}
*{box-sizing:border-box;margin:0;padding:0}
html,body{width:1200px;height:3627px;overflow:hidden}
body{position:relative;background:var(--white);font-family:"Catamaran",sans-serif;color:var(--text)}
.abs{position:absolute}
a{color:inherit;text-decoration:none}

/* hero */
.hero{left:0;top:0;width:1200px;height:716px;background:linear-gradient(90deg,#e9e7e5 0%,#dedbd8 45%,#cfcac6 100%)}
.hero-photo{left:600px;top:90px;width:600px;height:626px;background:linear-gradient(180deg,#d7d2cc 0%,#c4ccd8 50%,#9ea7b6 100%)}
.brand{left:99px;top:44px;font-family:"Catamaran",sans-serif;font-weight:700;font-size:32px;color:var(--orange)}
.nav{top:47px;font-family:"Barlow",sans-serif;font-weight:500;font-size:12px;letter-spacing:.3px;color:var(--orange);text-transform:uppercase}
.hero-title{left:99px;top:244px;font-weight:400;font-size:41px;line-height:44px;color:var(--orange)}
.hero-sub{left:99px;top:354px;font-weight:300;font-size:32px;line-height:36px;color:var(--ink)}
.btn{display:flex;align-items:center;justify-content:center;background:var(--orange);color:var(--white);font-family:"Barlow",sans-serif;font-weight:500;font-size:16px}
.hero-btn{left:99px;top:475px;width:155px;height:44px}

/* services */
.svc-icon{width:92px;height:72px}
.svc-label{font-weight:400;font-size:20px;line-height:20px;color:#8a8a8a}

/* intro */
.intro-title{left:98px;top:1258px;font-weight:500;font-size:30px;line-height:34px;color:var(--orange)}
.intro-list{left:98px;top:1340px;list-style:none;font-size:13px;line-height:16px;color:var(--muted)}
.intro-list li{position:relative;padding-left:19px}
.intro-list li::before{content:"";position:absolute;left:1px;top:5px;width:6px;height:6px;border-radius:50%;background:var(--orange)}
.house-art{left:500px;top:1156px;width:614px;height:340px;background:linear-gradient(180deg,#b9d0ea 0%,#d6dfe6 35%,#8fa07e 70%,#5f7a47 100%)}

.section-title{left:0;width:1200px;text-align:center;font-weight:500;font-size:31px;color:var(--orange)}

/* technicians */
.tech-card{top:1605px;width:228px;height:307px;background:var(--card);box-shadow:0 0 28px rgba(247,148,29,.18);text-align:center}
.tech-avatar{width:88px;height:88px;border-radius:50%;margin:16px auto 0;background:radial-gradient(circle at 50% 40%,#9fb4c8,#4d6274);box-shadow:3px 4px 8px rgba(247,148,29,.5)}
.tech-name{margin-top:8px;font-size:17px;font-weight:500;color:var(--orange);line-height:20px}
.tech-role{font-size:9px;color:#555;line-height:12px}
.tech-stars{margin-top:9px;font-size:15px;letter-spacing:2px;color:var(--orange);line-height:18px}
.tech-quote{margin:12px auto 0;width:172px;font-size:11px;line-height:13.5px;color:#333}
.tech-by{position:absolute;left:0;right:0;bottom:11px;font-size:11px;color:#333}

/* blog */
.post-img{top:2025px;height:160px}
.post-title{top:2211px;font-family:"Barlow",sans-serif;font-weight:600;font-size:15px;line-height:14px;color:var(--orange)}
.post-text{top:2250px;font-family:"Barlow",sans-serif;font-weight:600;font-size:15px;line-height:14px;color:var(--ink)}
.post-date{top:2297px;font-family:"Barlow",sans-serif;font-size:9px;color:var(--orange)}

/* partners */
.partner{top:2424px;font-family:"Barlow",sans-serif;font-weight:600;font-size:20px;color:#9a9a9a}
.more-btn{left:511px;top:2490px;width:177px;height:48px;border:1px solid var(--line);display:flex;align-items:center;justify-content:center;font-size:19px;color:#8a8a8a}
.press{top:2640px;font-family:"Barlow",sans-serif;font-weight:600;font-size:20px;color:#8c8c8c}

/* cities */
.city-col{top:2780px;font-size:13px;line-height:24px;color:#222}
.city-col b{font-weight:700}

/* call to action */
.cta{left:0;top:2995px;width:1200px;height:243px;background:linear-gradient(90deg,#f7a84a 0%,#f59a2e 60%,#f08a12 100%)}
.cta-photo{left:900px;top:2995px;width:300px;height:243px;background:linear-gradient(180deg,#f4b66a 0%,#e98f2c 100%)}
.cta-title{left:134px;top:3032px;font-weight:500;font-size:40px;line-height:48px;color:var(--white)}
.cta-sub{left:134px;top:3088px;font-weight:400;font-size:30px;line-height:34px;color:var(--ink)}
.cta-btn{left:135px;top:3165px;width:154px;height:43px}

/* footer */
.foot-col{top:3302px}
.foot-col h3{font-weight:500;font-size:16px;color:var(--orange);margin-bottom:1px}
.foot-col ul{list-style:none;font-size:13px;line-height:16.5px;color:#222}
.email{left:727px;top:3340px;width:235px;height:24px;border-bottom:1px solid var(--line);font-size:12px;color:#888;padding-top:6px}
.subscribe{left:981px;top:3322px;width:120px;height:38px}
.legal{top:3533px;font-size:13px;color:#222}
</style>
</head>
<body>

<!-- hero -->
<section class="abs hero"></section>
<div class="abs hero-photo" role="img" aria-label="Smiling technician in blue overalls holding a wrench in a bright kitchen"></div>
<div class="abs brand">Brava Nest</div>
<nav>
  <a class="abs nav" style="left:517px">Few tabs</a>
  <a class="abs nav" style="left:615px">About us</a>
  <a class="abs nav" style="left:708px">Contact us</a>
  <a class="abs nav" style="left:822px">Areas served</a>
  <a class="abs nav" style="left:961px;top:49px">Pricing and services</a>
</nav>
<h1 class="abs hero-title">Home maintenance<br>made simple</h1>
<p class="abs hero-sub">The best technicians in<br>your neighborhood.</p>
<a class="abs btn hero-btn">Book a Servive</a>

<!-- services -->
<svg class="abs svc-icon" style="left:203px;top:778px" viewBox="0 0 92 72" fill="none" stroke="#f7941d" stroke-width="2"><rect x="2" y="2" width="86" height="58"/><line x1="38" y1="66" x2="52" y2="66"/><line x1="45" y1="60" x2="45" y2="66"/></svg>
<div class="abs svc-label" style="left:316px;top:793px">TV<br>Mounthing</div>

<svg class="abs svc-icon" style="left:510px;top:782px" viewBox="0 0 92 72" fill="none" stroke="#f7941d" stroke-width="2"><path d="M14 10h22v10H14z"/><path d="M20 20v8l-6 10v30h30V38l-6-10v-8"/><path d="M36 14h8"/><path d="M8 6l4 2M8 14h4M8 22l4-2"/></svg>
<div class="abs svc-label" style="left:598px;top:800px">Disinfection<br>Spray</div>

<svg class="abs svc-icon" style="left:785px;top:780px" viewBox="0 0 92 72" fill="none" stroke="#f7941d" stroke-width="2"><path d="M2 4h10v20H2z"/><path d="M12 10h30v14h16v12H44V24"/><path d="M12 18h22"/><path d="M52 50c-4 6-4 10 0 12 4-2 4-6 0-12z"/></svg>
<div class="abs svc-label" style="left:880px;top:792px">Plumbing<br>Services</div>

<svg class="abs svc-icon" style="left:205px;top:895px" viewBox="0 0 92 72" fill="none" stroke="#f7941d" stroke-width="2"><rect x="2" y="2" width="56" height="66" rx="3"/><line x1="2" y1="14" x2="58" y2="14"/><circle cx="30" cy="41" r="19"/><circle cx="30" cy="41" r="12"/><rect x="38" y="6" width="14" height="4"/></svg>
<div class="abs svc-label" style="left:316px;top:920px">Home<br>Appliances</div>

<svg class="abs svc-icon" style="left:515px;top:888px" viewBox="0 0 92 72" fill="none" stroke="#f7941d" stroke-width="2"><rect x="2" y="2" width="36" height="64" rx="4"/><line x1="2" y1="12" x2="38" y2="12"/><line x1="2" y1="54" x2="38" y2="54"/><circle cx="20" cy="60" r="2"/></svg>
<div class="abs svc-label" style="left:598px;top:900px">Phone<br>Repair</div>

<svg class="abs svc-icon" style="left:783px;top:890px" viewBox="0 0 92 72" fill="none" stroke="#f7941d" stroke-width="2"><path d="M2 20L38 2l36 18v48H2z"/><rect x="10" y="26" width="56" height="42"/><path d="M10 34h56M10 42h56M10 50h56M10 58h56"/></svg>
<div class="abs svc-label" style="left:880px;top:912px">Garage Door<br>Repair</div>

<svg class="abs svc-icon" style="left:205px;top:1012px" viewBox="0 0 92 72" fill="none" stroke="#f7941d" stroke-width="2"><rect x="2" y="12" width="78" height="50"/><path d="M30 12V4h22v8"/><line x1="2" y1="34" x2="80" y2="34"/><rect x="36" y="30" width="10" height="8"/></svg>
<div class="abs svc-label" style="left:316px;top:1028px">Handy<br>Servies</div>

<svg class="abs svc-icon" style="left:515px;top:1012px" viewBox="0 0 92 72" fill="none" stroke="#f7941d" stroke-width="2"><path d="M4 32L32 4l28 28"/><path d="M10 26v40h44V26"/><path d="M44 12V6h6v12"/><path d="M20 40a17 17 0 0 1 24 0M24 46a11 11 0 0 1 16 0M28 52a5 5 0 0 1 8 0"/></svg>
<div class="abs svc-label" style="left:600px;top:1028px">Smart Home<br>Installation</div>

<!-- intro -->
<h2 class="abs intro-title">A simple way to take care<br>of everything</h2>
<ul class="abs intro-list">
  <li>Trusted technicians in your neighborhood</li>
  <li>Guaranteed parts and service + 24/7 support</li>
  <li>Hundreds of repair and install option</li>
</ul>
<div class="abs house-art" role="img" aria-label="Illustrated two-storey house with labels for smart home, TV mounting, HVAC, appliances, plumbing, security and garage door services"></div>

<!-- technicians -->
<h2 class="abs section-title" style="top:1528px">Our top technicians are in your neighborhood and beyond</h2>

<article class="abs tech-card" style="left:217px">
  <div class="tech-avatar" role="img" aria-label="Portrait of technician Marcus Dale"></div>
  <div class="tech-name">Marcus Dale</div>
  <div class="tech-role">Brava Nest technician</div>
  <div class="tech-stars">★★★★★</div>
  <p class="tech-quote">"BravaNest was quick, affordable, and extremely convenient! Marcus was my tech and he was great. Would 100% use BravaNest again!"</p>
  <div class="tech-by">Alina | Los Angeles, CA</div>
</article>
<article class="abs tech-card" style="left:486px">
  <div class="tech-avatar" role="img" aria-label="Portrait of technician Jonah Keller"></div>
  <div class="tech-name">Jonah Keller</div>
  <div class="tech-role">Brava Nest technician</div>
  <div class="tech-stars">★★★★★</div>
  <p class="tech-quote">"This is one of the best services around. Jonah, my tech, was punctual, courteous and efficient. Will definitely use BravaNest again."</p>
  <div class="tech-by">Dario | Colton, CA</div>
</article>
<article class="abs tech-card" style="left:755px">
  <div class="tech-avatar" role="img" aria-label="Portrait of technician Samir Tovar"></div>
  <div class="tech-name">Samir Tovar</div>
  <div class="tech-role">Brava Nest technician</div>
  <div class="tech-stars">★★★★★</div>
  <p class="tech-quote">"I'm impressed at the efficiency of this company. Samir was a real MVP, super professional and friendly."</p>
  <div class="tech-by">Selim | Houston, TX</div>
</article>

<!-- blog -->
<h2 class="abs section-title" style="top:1950px">The beat - the BravaNest blog</h2>

<div class="abs post-img" style="left:209px;width:221px;background:linear-gradient(180deg,#6f8fa8 0%,#3d4f5e 55%,#4e6b35 100%)" role="img" aria-label="Craftsman house with a lit porch at dusk"></div>
<div class="abs post-title" style="left:211px">Hottest Parts of the House to<br>Remodel In Summer 2020</div>
<div class="abs post-text" style="left:211px">The summer is the perfect time<br>to remodel your...</div>
<div class="abs post-date" style="left:211px">May 2020</div>

<div class="abs post-img" style="left:496px;width:233px;background:linear-gradient(180deg,#f3b562 0%,#a9602a 50%,#3e2616 100%)" role="img" aria-label="Covered patio with outdoor furniture at sunset"></div>
<div class="abs post-title" style="left:496px">Hottest Parts of the House to<br>Remodel In Summer 2020</div>
<div class="abs post-text" style="left:496px">The summer is the perfect time<br>to remodel your...</div>
<div class="abs post-date" style="left:496px">May 2020</div>

<div class="abs post-img" style="left:803px;width:199px;background:linear-gradient(180deg,#cfd8de 0%,#a9b9c4 50%,#d8c4a8 100%)" role="img" aria-label="Family baking together in a bright kitchen"></div>
<div class="abs post-title" style="left:803px;top:2209px">Hottest Parts of the House to<br>Remodel In Summer 2020</div>
<div class="abs post-text" style="left:803px;top:2248px">The summer is the perfect time<br>to remodel your...</div>
<div class="abs post-date" style="left:803px;top:2295px">May 2020</div>

<!-- trusted by -->
<h2 class="abs section-title" style="top:2358px;font-weight:400;font-size:29px">Trusted by</h2>
<div class="abs partner" style="left:360px">Northpoint</div>
<div class="abs partner" style="left:514px">Lumora</div>
<div class="abs partner" style="left:640px">Vextra</div>
<div class="abs partner" style="left:742px">Guardly</div>
<a class="abs more-btn">And many more</a>

<!-- featured in -->
<h2 class="abs section-title" style="top:2572px;font-weight:400;font-size:29px">Featured In</h2>
<div class="abs press" style="left:207px">The Daily Ledger</div>
<div class="abs press" style="left:442px">MarketWire</div>
<div class="abs press" style="left:600px">Venturo</div>
<div class="abs press" style="left:710px;font-size:17px;top:2643px">The Metro Courier</div>
<div class="abs press" style="left:866px">TechPulse</div>

<!-- cities -->
<h2 class="abs section-title" style="top:2707px;font-weight:400;font-size:30px">Cities where BravaNest is available:</h2>
<div class="abs city-col" style="left:271px"><b>Arizona</b><br>Phoenix<br><b>Colorado</b><br>Denver</div>
<div class="abs city-col" style="left:408px"><b>Florida</b><br>Miami<br>Orlando<br>Tampa<br><b>Georgia</b><br>Atlanta</div>
<div class="abs city-col" style="left:544px"><b>Illinois</b><br>Chicago<br><b>Massachusetts</b><br>Boston<br><b>Nevada</b><br>Las Vegas</div>
<div class="abs city-col" style="left:682px"><b>North Carolina</b><br>Charlotte<br><b>Pennsylvania</b><br>Philadelphia</div>
<div class="abs city-col" style="left:819px"><b>Texas</b><br>Austin<br>Dallas<br>Houston<br>San Antonio<br><b>Washington D.C.</b><br>Washington, D.C.</div>

<!-- call to action -->
<section class="abs cta"></section>
<div class="abs cta-photo" role="img" aria-label="Cheerful technician with a tool belt in a kitchen"></div>
<h2 class="abs cta-title">Ready to get started?</h2>
<p class="abs cta-sub">Repair or install<br>a device today.</p>
<a class="abs btn cta-btn">Book a Service</a>

<!-- footer -->
<div class="abs foot-col" style="left:98px"><h3>Company</h3><ul><li>About Us</li><li>How it Works</li><li>Become a Tech</li><li>Pricing</li><li>Careers</li><li>Blog</li><li>Newsroom</li><li>Media inquiries</li><li>Home</li></ul></div>
<div class="abs foot-col" style="left:310px"><h3>Resources</h3><ul><li>TV Mounting</li><li>Garage Doors</li><li>Appliances</li><li>Refrigerators</li><li>Dishwashers</li><li>Ovens &amp; Stoves</li><li>Washing Machines</li><li>Dryers</li><li>Plumbing</li></ul></div>
<div class="abs foot-col" style="left:501px"><h3>Partnerships</h3><ul><li>Searchly</li><li>Vextra</li><li>Guardly</li><li>Lumora</li><li>Trovely for business</li><li>Legals</li><li>Privacy</li><li>Terms</li><li>Guarantee</li></ul></div>
<div class="abs foot-col" style="left:727px"><h3>Stay in Touch</h3></div>
<div class="abs email">Enter email</div>
<a class="abs btn subscribe">Subscribe</a>

<div class="abs legal" style="left:98px">©Brava Nest Inc 2020</div>
<div class="abs legal" style="right:90px">Brava Nest Inc. is not in any way associated with BravaNest GmbH of Lindau</div>

</body>
</html>
```